Business Card Design

We would like a business card that utilizes our current logo and keeps with the same feel - elegant and organic. Our farm isn't about mass production, it's about excellence, education, beautiful events and flowers - people, culture, and community.

Target Market(s)

Patrons to our farm who are interested in weddings, events, or our flowers and vegetables.

Contact Information for Business Card

Name, address, cell email (Rosalind Hepworth, 2718 Wintervale Rd, Harlow Ridge, NE 80517, cell 30.412.6387, email rosalind@wintervalefarm.example)

```html
<!DOCTYPE html>
<html lang="en">
<head>
<meta charset="utf-8">
<title>Wintervale Farm – Business Card</title>
<link rel="stylesheet" href="https://fonts.googleapis.com/css2?family=Libre+Baskerville:wght@400;700&display=swap">
<style>
  :root {
    --backdrop: #3b3b3b;
    --sage: #6e9479;
    --sage-deep: #557a60;
    --sage-faint: #7ea088;
    --paper: #ffffff;
    --ink: #5a5a5a;
    --copper: #b07a3c;
    --name-green: #5f8a69;
  }
  * { box-sizing: border-box; margin: 0; padding: 0; }
  html, body { width: 1200px; height: 1056px; overflow: hidden; }
  body {
    background: var(--backdrop);
    font-family: "Libre Baskerville", Georgia, serif;
    position: relative;
  }
  .card {
    position: absolute;
    left: 285px;
    width: 630px;
    height: 360px;
    overflow: hidden;
    box-shadow: 0 14px 30px rgba(0,0,0,0.35);
  }
  .card--front { top: 120px; background: var(--sage); }
  .card--back { top: 560px; background: var(--paper); }

  .front-foliage {
    position: absolute;
    left: 40px; top: 30px;
    width: 300px; height: 280px;
    border-radius: 50% 40% 45% 50%;
    background: radial-gradient(ellipse at center, var(--sage-faint) 0%, rgba(126,160,136,0) 70%);
  }
  .front-wordmark {
    position: absolute;
    right: 70px; top: 150px;
    text-align: right;
    color: var(--paper);
    font-weight: 400;
  }
  .front-wordmark .brand-name { font-size: 40px; letter-spacing: 1px; display: block; }

  .back-wordmark {
    position: absolute;
    left: 60px; top: 60px;
    color: var(--sage-deep);
    font-weight: 400;
  }
  .back-wordmark .brand-name { font-size: 38px; letter-spacing: 1px; display: block; }

  .back-foliage {
    position: absolute;
    right: 30px; top: 30px;
    width: 160px; height: 210px;
    border-radius: 45% 50% 40% 50%;
    background: radial-gradient(ellipse at center, var(--sage) 0%, rgba(110,148,121,0.25) 60%, rgba(110,148,121,0) 75%);
  }

  .contact {
    position: absolute;
    left: 60px; bottom: 42px;
    color: var(--ink);
    font-size: 14px;
  }
  .contact__name {
    color: var(--name-green);
    font-weight: 700;
    font-size: 28px;
    margin-bottom: 12px;
  }
  .contact__row { display: flex; align-items: center; gap: 22px; margin-bottom: 8px; }
  .contact__item { display: flex; align-items: center; gap: 8px; white-space: nowrap; }
  .icon {
    width: 18px; height: 18px;
    background: var(--copper);
    border-radius: 3px;
    display: flex; align-items: center; justify-content: center;
  }
  .icon svg { width: 12px; height: 12px; fill: none; stroke: var(--paper); stroke-width: 1.6; stroke-linecap: round; stroke-linejoin: round; }
</style>
</head>
<body>

  <section class="card card--front" aria-label="Business card front">
    <div class="front-foliage" role="img" aria-label="Faint leafy branch illustration"></div>
    <div class="front-wordmark">
      <span class="brand-name">Wintervale Farm</span>
    </div>
  </section>

  <section class="card card--back" aria-label="Business card back">
    <div class="back-foliage" role="img" aria-label="Green leafy branch illustration"></div>
    <div class="back-wordmark">
      <span class="brand-name">Wintervale Farm</span>
    </div>

    <div class="contact">
      <p class="contact__name">Rosalind Hepworth</p>
      <div class="contact__row">
        <span class="contact__item">
          <span class="icon"><svg viewBox="0 0 12 12"><path d="M3 1.5 L4.5 4 L3.5 5 Q4.5 7.5 7 8.5 L8 7.5 L10.5 9 L9.5 10.5 Q4 10 1.5 2.5 Z"/></svg></span>
          30.412.6387
        </span>
        <span class="contact__item">
          <span class="icon"><svg viewBox="0 0 12 12"><rect x="1.5" y="3" width="9" height="6.5"/><path d="M1.5 3 L6 7 L10.5 3"/></svg></span>
          rosalind@wintervalefarm.example
        </span>
      </div>
      <div class="contact__row">
        <span class="contact__item">
          <span class="icon"><svg viewBox="0 0 12 12"><path d="M6 11 Q2 6.5 2 4.5 A4 4 0 0 1 10 4.5 Q10 6.5 6 11 Z"/><circle cx="6" cy="4.5" r="1.3"/></svg></span>
          2718 Wintervale Rd, Harlow Ridge, NE 80517
        </span>
      </div>
    </div>
  </section>

</body>
</html>
```